Startup online payment business - Sporting / Golf, Swift Tee payment

Background:
Our business name is "Swift Tee" we provide online payments for golfing services via our website. We currently have a logo used on our website. No other design style has been developed. Our aim is to remove cash payments for service at golf clubs.

Our Key Values:
Quick and easy
Formal and polite
Fun with professional boundary
Mate-ship relationships
100% online digital

What we want from you:
Marketing design to be used on posters and stickers in a retail setting to direct customers to our online payment Chanel.
Design must incorporate attached logo, URL swifttee.com.au and our key values can act as a guide the type of design. We have used color Hex#007672 for logo background. We are open to use other colors.

Target Market(s)

Golf clubs and golf players

Industry/Entity Type

Golf Course

Font styles to use
Sans Serif

Requirements
Must have
• Directions to online payment via URL: swifttee.com.au
Nice to have
• We like the idea of the slogan: No Cash - No worries. Have attached home screen that will be available from URL link. Consideration if using mobile phone in image. Push the online payment and steps 1. Visit swifttee.com 2. Select club 3. Confirm payment
Should not have
• Cartoons

```html
<!DOCTYPE html>
<html lang="en">
<head>
<meta charset="utf-8">
<title>Swift Tee – No Cash Poster</title>
<link rel="stylesheet" href="https://fonts.googleapis.com/css2?family=Roboto:wght@400;500;700;900&display=swap">
<style>
  :root {
    --teal: #007672;
    --teal-dark: #1e7a6e;
    --teal-grey: #5f9c96;
    --green-dark: #2e8b57;
    --green: #3fa444;
    --green-light: #5cc05c;
    --gold: #e0a23a;
    --gold-dark: #b9822a;
    --sky-top: #ffffff;
    --sky-bottom: #8fb0ea;
    --grass: #6fae3c;
    --stage: #d4d5dc;
    --ball: #f1f1f1;
    --white: #ffffff;
  }
  * { box-sizing: border-box; margin: 0; padding: 0; }
  html, body { width: 1200px; height: 1200px; overflow: hidden; }
  body { background: var(--stage); font-family: "Roboto", Arial, sans-serif; }

  .poster {
    position: absolute; left: 136px; top: 0;
    width: 928px; height: 1200px; overflow: hidden;
    background: linear-gradient(180deg, var(--sky-top) 190px, #dfe8f8 380px, var(--sky-bottom) 760px, #9dbbee 1000px);
  }
  .header {
    position: absolute; left: 0; top: 0; width: 100%; height: 188px;
    background: var(--teal);
  }
  .brand {
    position: absolute; left: 38px; top: 40px; width: 200px;
    color: var(--white); font-weight: 700; font-size: 46px; line-height: 1.05;
    letter-spacing: 3px; text-transform: uppercase;
  }
  .intro {
    position: absolute; left: 282px; top: 24px; width: 623px;
    color: var(--white); font-size: 15.2px; font-weight: 500; line-height: 20px;
    text-align: justify;
  }
  .course-photo {
    position: absolute; left: 0; top: 960px; width: 100%; height: 240px;
    background: linear-gradient(180deg, #3f6a3a 0%, #4f7d3b 35%, var(--grass) 60%, #8cc04a 100%);
  }
  .phone-photo {
    position: absolute; left: 0; top: 893px; width: 305px; height: 307px;
    background: linear-gradient(160deg, #3a3a3c 0%, var(--teal) 45%, #d9a98a 80%);
    border-top-right-radius: 40px;
  }
  .graphics { position: absolute; left: 0; top: 0; width: 928px; height: 1200px; }
  .slogan {
    position: absolute; left: 75px; top: 152px; width: 785px; height: 70px;
    display: flex; align-items: center; justify-content: center;
    color: var(--white); font-weight: 900; font-size: 53px; letter-spacing: 0.5px;
  }
  .value-label {
    position: absolute; width: 180px; text-align: center;
    font-weight: 700; font-size: 19px; line-height: 21px;
  }
  .key-values {
    position: absolute; left: 368px; top: 548px; width: 200px; text-align: center;
    color: var(--teal); font-weight: 900; font-size: 34px; line-height: 36px;
  }
  .key-values span { display: inline-block; border-bottom: 2px solid var(--teal); padding-bottom: 2px; }
  .register {
    position: absolute; left: 345px; top: 918px; width: 567px;
    color: var(--teal); font-size: 15.2px; font-weight: 500; line-height: 20px;
  }
  .url-pill {
    position: absolute; left: 272px; top: 1140px; width: 450px; height: 46px;
    background: var(--gold); border: 2px solid var(--white); border-radius: 24px;
    display: flex; align-items: center; justify-content: center; gap: 12px;
    color: var(--white); font-weight: 700; font-size: 29px;
  }
</style>
</head>
<body>
<main class="poster">
  <div class="course-photo" role="img" aria-label="Photo of a golf fairway lined with pine trees and bunkers"></div>
  <div class="phone-photo" role="img" aria-label="Photo of a hand holding a mobile phone showing the Swift Tee app"></div>

  <header class="header">
    <div class="brand">Swift Tee</div>
    <p class="intro">Swift Tee is here to support Golf Clubs embrace new strategies for success in a rapidly changing world. Moving toward a future cashless society, Swift Tee are developing new mobile payment methods in order for Clubs to cater for the next generation of players and community expectations. Interested in learning more about how we can help grow your Clubs earning potential?</p>
  </header>

  <svg class="graphics" viewBox="0 0 928 1200" aria-hidden="true">
    <defs>
      <radialGradient id="ball" cx="40%" cy="35%" r="70%">
        <stop offset="0" stop-color="#ffffff"/>
        <stop offset="1" stop-color="#dcdcdc"/>
      </radialGradient>
    </defs>
    <!-- ribbon tails -->
    <polygon points="18,208 92,208 110,272 18,272 44,240" fill="var(--gold-dark)"/>
    <polygon points="75,208 92,208 110,272 75,222" fill="#8a5f1c"/>
    <polygon points="910,208 836,208 818,272 910,272 884,240" fill="var(--gold-dark)"/>
    <polygon points="853,208 836,208 818,272 853,222" fill="#8a5f1c"/>
    <rect x="75" y="152" width="785" height="70" fill="var(--gold)"/>

    <!-- connecting band -->
    <polygon points="468,362 695,523 606,790 327,790 245,520" fill="none" stroke="var(--green)" stroke-width="80" stroke-linejoin="round"/>
    <polygon points="468,362 695,523 606,790 327,790 245,520" fill="none" stroke="var(--teal-dark)" stroke-width="80" stroke-linejoin="round" stroke-dasharray="0 900 260 2000" opacity="0.6"/>
    <polygon points="468,362 695,523 606,790 327,790 245,520" fill="var(--sky-bottom)" opacity="0"/>

    <!-- value circles -->
    <g>
      <circle cx="468" cy="362" r="108" fill="var(--green-dark)"/>
      <circle cx="468" cy="362" r="92" fill="var(--white)"/>
      <circle cx="468" cy="362" r="86" fill="url(#ball)"/>
      <circle cx="695" cy="523" r="108" fill="var(--green-light)"/>
      <circle cx="695" cy="523" r="92" fill="var(--white)"/>
      <circle cx="695" cy="523" r="86" fill="url(#ball)"/>
      <circle cx="606" cy="790" r="108" fill="var(--green)"/>
      <circle cx="606" cy="790" r="92" fill="var(--white)"/>
      <circle cx="606" cy="790" r="86" fill="url(#ball)"/>
      <circle cx="327" cy="790" r="108" fill="var(--teal-dark)"/>
      <circle cx="327" cy="790" r="92" fill="var(--white)"/>
      <circle cx="327" cy="790" r="86" fill="url(#ball)"/>
      <circle cx="245" cy="520" r="108" fill="var(--teal-grey)"/>
      <circle cx="245" cy="520" r="92" fill="var(--white)"/>
      <circle cx="245" cy="520" r="86" fill="url(#ball)"/>
      <circle cx="468" cy="598" r="108" fill="var(--teal)"/>
      <circle cx="468" cy="598" r="98" fill="var(--white)"/>
      <circle cx="468" cy="598" r="93" fill="url(#ball)"/>
    </g>

    <!-- thumbs up -->
    <g fill="none" stroke="var(--green-dark)" stroke-width="4" stroke-linejoin="round" stroke-linecap="round">
      <rect x="434" y="320" width="16" height="50"/>
      <path d="M450 325 L466 312 L470 295 Q480 292 480 305 L476 322 L506 322 Q514 324 510 334 Q516 340 508 346 Q514 352 506 358 Q510 366 500 370 L450 370"/>
      <path d="M478 290 L476 282 M488 294 L494 287 M468 292 L462 286"/>
    </g>
    <!-- star -->
    <g fill="none" stroke="var(--green)" stroke-width="4" stroke-linejoin="round" stroke-linecap="round">
      <polygon points="604,705 616,730 643,733 623,751 628,777 604,764 580,777 585,751 565,733 592,730"/>
      <path d="M604 783 L604 790 M568 714 L563 709 M640 714 L645 709 M556 752 L549 754 M652 752 L659 754"/>
    </g>
    <!-- phone with money -->
    <g fill="none" stroke="var(--teal-grey)" stroke-width="3.5" stroke-linejoin="round">
      <rect x="212" y="445" width="52" height="88" rx="6"/>
      <path d="M230 452 L246 452"/>
      <rect x="240" y="465" width="54" height="42" rx="3" fill="#eef3f2"/>
      <circle cx="264" cy="486" r="11"/>
    </g>
    <text x="264" y="492" text-anchor="middle" font-family="Roboto, sans-serif" font-weight="700" font-size="15" fill="var(--teal-grey)">$</text>
    <!-- people icon placeholders -->
    <rect x="640" y="460" width="110" height="70" rx="10" fill="var(--green)" opacity="0.85" role="img" aria-label="Icon of three business people"/>
    <rect x="290" y="728" width="76" height="64" rx="10" fill="var(--teal-dark)" opacity="0.85" role="img" aria-label="Icon of two people giving a high five"/>
    <!-- globe -->
  </svg>

  <div class="slogan">NO CASH - NO WORIES!</div>

  <div class="value-label" style="left:378px; top:382px; color:var(--green-dark);">Quick<br>&amp; Easy</div>
  <div class="value-label" style="left:605px; top:540px; color:var(--green);">Formal<br>&amp; Polite</div>
  <div class="value-label" style="left:516px; top:797px; color:var(--green);">Fun with<br>Professional<br>Boundary</div>
  <div class="value-label" style="left:237px; top:795px; color:var(--teal-dark);">Mate-ship<br>Relationships</div>
  <div class="value-label" style="left:148px; top:540px; color:var(--teal-grey);">100%<br>Online Digital</div>
  <div class="key-values"><span>KEY<br>VALUES</span></div>

  <p class="register">Please visit our website to register your interest now and a member of the Swift Tee team will be in contact to advise of the services and benefits on offer.</p>

  <div class="url-pill">
    <svg width="30" height="30" viewBox="0 0 30 30" aria-hidden="true" fill="none" stroke="#fff" stroke-width="2.2">
      <circle cx="15" cy="15" r="12"/>
      <ellipse cx="15" cy="15" rx="5.5" ry="12"/>
      <path d="M3 15 H27 M5 9 H25 M5 21 H25"/>
    </svg>
    <span>swifttee.com.au</span>
  </div>
</main>
</body>
</html>
```